One of Australia's fastest growing Financial Company looking for an updated business card design!

Meridale Holdings Australia is looking for an updated design for our business cards. We would like to keep up our professional appearances and have get new exciting design that fits our company.

The Meridale aim is to facilitate and assist clients in every financial requirement that may arise in financial areas.

We would to see the design to use colour blue and we like the clouds in the background. We have attached two designs we have use before but we need something with more professional and easy to read design.

We would like the website in the back of the card; the employees name more central and stands out; only a postal address; a list of all our locations along the bottom (Sydney, Melbourne, Brisbane, Singapore)

Looking forward to seeing the designs come in!

Target Market(s)

Other Industry Professionals
Middle Class Families

Industry/Entity Type

Finance

Contact Information for Business Card

Name; Company Role; Office Number; Mobile Number; Email Address; Website; Postal Address; Locations

Font styles to use
Serif
Sans Serif

Colors
0492cd
33a6d7
85cae6
85acd3
3176b5
0455a3
cee9f5
d5e2ee

Requirements
Must have
• Name; Company Role; Office Number; Mobile Number; Email Address; Website; Postal Address; Locations
Nice to have
• The colour blue, clouds on the background

```html
<!DOCTYPE html>
<html lang="en">
<head>
<meta charset="utf-8">
<title>Meridale Holdings Australia – Business Card</title>
<link rel="stylesheet" href="https://fonts.googleapis.com/css2?family=Montserrat:wght@400;500;600&display=swap">
<style>
  :root {
    --page-bg: #9a9a9a;
    --blue-deep: #0455a3;
    --blue-mid: #3176b5;
    --blue-bright: #0492cd;
    --blue-sky: #85acd3;
    --band: #cee9f5;
    --band-line: #d5e2ee;
    --ink-dark: #0b1f3a;
    --white: #ffffff;
  }
  * { margin: 0; padding: 0; box-sizing: border-box; }
  html, body { width: 1200px; height: 800px; overflow: hidden; }
  body {
    background: var(--page-bg);
    font-family: "Montserrat", sans-serif;
    display: flex;
    align-items: center;
    justify-content: center;
    gap: 50px;
  }
  .card {
    position: relative;
    width: 540px;
    height: 330px;
    overflow: hidden;
    box-shadow: 0 6px 18px rgba(0,0,0,0.25);
    color: var(--white);
  }

  /* Back */
  .card-back {
    background: linear-gradient(160deg, var(--blue-mid) 0%, var(--blue-deep) 70%);
  }
  .sky {
    position: absolute; inset: 0;
    background:
      radial-gradient(ellipse 200px 60px at 78% 14%, rgba(220,232,248,0.55), transparent 70%),
      linear-gradient(160deg, var(--blue-mid) 0%, var(--blue-deep) 75%);
  }
  .back-content {
    position: absolute; inset: 0;
    display: flex; flex-direction: column;
    align-items: center; justify-content: center;
    gap: 30px;
  }
  .brand {
    display: flex; align-items: center; gap: 14px;
    font-weight: 500; color: var(--white);
  }
  .brand-dot { border-radius: 50%; background: var(--white); }
  .brand-lg { font-size: 62px; }
  .brand-lg .brand-dot { width: 34px; height: 34px; }
  .back-web { font-size: 17px; font-weight: 500; letter-spacing: 0.3px; }

  /* Front */
  .card-front {
    background:
      radial-gradient(ellipse 260px 120px at 55% 0%, rgba(133,202,230,0.25), transparent 70%),
      linear-gradient(160deg, var(--blue-mid) 0%, var(--blue-deep) 70%);
  }
  .front-brand {
    position: absolute; top: 42px; right: 30px;
  }
  .brand-sm { font-size: 38px; gap: 10px; }
  .brand-sm .brand-dot { width: 22px; height: 22px; }
  .person {
    position: absolute; top: 92px; left: 34px;
  }
  .person-name { font-size: 27px; font-weight: 500; letter-spacing: 0.5px; }
  .person-role { font-size: 15px; margin-top: 2px; }
  .contact-list {
    position: absolute; top: 160px; left: 36px;
    list-style: none;
    font-size: 15.5px; line-height: 1.45;
  }
  .contact-list li { display: flex; align-items: flex-start; gap: 14px; }
  .contact-list svg { width: 18px; height: 18px; flex: none; margin-top: 3px; fill: var(--white); }
  .contact-list .gap { width: 18px; flex: none; }
  .footer-band {
    position: absolute; left: 0; right: 0; bottom: 0; height: 46px;
    background: var(--band);
    border-top: 3px solid var(--band-line);
    display: flex; align-items: center; justify-content: center;
  }
  .footer-band::before {
    content: ""; position: absolute; left: 0; right: 0; top: -8px;
    height: 2px; background: var(--band-line);
  }
  .front-web { color: var(--ink-dark); font-size: 16px; font-weight: 500; }
</style>
</head>
<body>

  <section class="card card-back" aria-label="Card back">
    <div class="sky" role="img" aria-label="Blue sky with soft white clouds"></div>
    <div class="back-content">
      <div class="brand brand-lg"><span class="brand-dot"></span>Meridale</div>
      <p class="back-web">www.meridaleholdings.com.au</p>
    </div>
  </section>

  <section class="card card-front" aria-label="Card front">
    <div class="brand brand-sm front-brand"><span class="brand-dot"></span>Meridale</div>

    <div class="person">
      <h1 class="person-name">JOANNA PRYCE</h1>
      <p class="person-role">Investment Consultant</p>
    </div>

    <ul class="contact-list">
      <li>
        <svg viewBox="0 0 24 24" aria-hidden="true"><path d="M6.6 10.8a15.1 15.1 0 0 0 6.6 6.6l2.2-2.2a1 1 0 0 1 1-.25 11.4 11.4 0 0 0 3.6.57 1 1 0 0 1 1 1V20a1 1 0 0 1-1 1A17 17 0 0 1 3 4a1 1 0 0 1 1-1h3.5a1 1 0 0 1 1 1c0 1.25.2 2.45.57 3.57a1 1 0 0 1-.25 1z"/></svg>
        (02) 5550 0147
      </li>
      <li>
        <svg viewBox="0 0 24 24" aria-hidden="true"><path d="M7 2h10a2 2 0 0 1 2 2v16a2 2 0 0 1-2 2H7a2 2 0 0 1-2-2V4a2 2 0 0 1 2-2zm0 3v13h10V5zm5 14.2a1 1 0 1 0 0 .01z"/></svg>
        (04) 555 218 406
      </li>
      <li>
        <svg viewBox="0 0 24 24" aria-hidden="true"><path d="M3 5h18a1 1 0 0 1 1 1v12a1 1 0 0 1-1 1H3a1 1 0 0 1-1-1V6a1 1 0 0 1 1-1zm1 2.2V17h16V7.2l-8 5.3z M4.5 7l7.5 5 7.5-5z"/></svg>
        meridaleholdings.com.au
      </li>
      <li>
        <svg viewBox="0 0 24 24" aria-hidden="true"><path d="M12 2a7 7 0 0 1 7 7c0 5.2-7 13-7 13S5 14.2 5 9a7 7 0 0 1 7-7zm0 4.5a2.5 2.5 0 1 0 0 5 2.5 2.5 0 0 0 0-5z"/></svg>
        Harbourside Post Shop PO BOX 1180
      </li>
      <li><span class="gap"></span>(Sydney, Melbourne, Brisbane, Singapore)</li>
    </ul>

    <div class="footer-band">
      <p class="front-web">www.meridaleholdings.com.au</p>
    </div>
  </section>

</body>
</html>
```